Dishwashing salt packaging label

We need a packaging label design for dishwasher salt. The product prevents lime, calcium and other mineral buildups in dishwashers as well as softening the water for the best washing results possible.

The brand name is Tarkozel.

As part of the design a logo and colour scheme/theme are required.
Updates

Project Deadline Extended
Reason: Need more time to provide feedback to designers.

Target Market(s)

25-55 year olds

Industry/Entity Type

Product

Requirements
Must have
• The packaging is in the form of a pail. The design should be in the form of labels that are stuck on to the area below the flange. The design should also be provided in a format that allows a printer to manipulate the images for printing.

The pail dimensions are shown in the attached pail_specification.pdf file. The pail size is the 2 litre size. An image of the pail is shown in the attached Pail_Image.jpeg file.

Not shown in the pdf document are the following dimensions:

Height from base to flange: 126mm
Diameter directly below the flange: 150mm

The label should have the following information on it:

Australian Owned and Manufactured
www.tarkozel.com.au
17 Maddock St, Kelbury Heights, Queensland, Australia

I would also like to be provided with images of the logo design and elements of the label design separately.

Nice to have
• If you consider that any slogan or other wording is necessary or desirable on the packaging, suggestions are welcome.

The design should look modern and clean.

```html
<!DOCTYPE html>
<html lang="en">
<head>
<meta charset="utf-8">
<title>Tarkozel Dishwasher Salt – Pail Label</title>
<link href="https://fonts.googleapis.com/css2?family=Archivo:ital,wght@0,500;0,800;1,800&family=Libre+Baskerville:wght@700&display=swap" rel="stylesheet">
<style>
  :root {
    --page: #f3f5f8;
    --blue-deep: #1f4fae;
    --blue-mid: #3f78d0;
    --blue-light: #a9c8ef;
    --blue-pale: #dce9f8;
    --navy: #18367f;
    --white: #ffffff;
    --ink: #0f1a33;
  }
  html, body {
    margin: 0;
    width: 1200px;
    height: 1200px;
    overflow: hidden;
    background: var(--page);
  }
  .label {
    position: absolute;
    left: 50px;
    top: 340px;
    width: 1100px;
    height: 520px;
    overflow: hidden;
    border-radius: 6px;
    box-shadow: 0 10px 30px rgba(20, 40, 90, 0.18);
  }
  .label-art {
    position: absolute;
    inset: 0;
    width: 1100px;
    height: 520px;
  }
  .origin-tag {
    position: absolute;
    left: 300px;
    top: 38px;
    width: 310px;
    height: 40px;
    background: var(--navy);
    color: var(--white);
    font: 500 15px/40px "Archivo", sans-serif;
    text-align: center;
  }
  .brand-name {
    position: absolute;
    left: 110px;
    top: 128px;
    width: 760px;
    text-align: center;
    color: var(--white);
    font: 800 108px/1 "Archivo", sans-serif;
    letter-spacing: -1px;
  }
  .product-name {
    position: absolute;
    left: 110px;
    top: 256px;
    width: 760px;
    text-align: center;
    color: var(--blue-pale);
    font: italic 800 44px/1 "Archivo", sans-serif;
  }
  .weight-panel {
    position: absolute;
    right: 40px;
    top: 380px;
    width: 170px;
    height: 80px;
    background: var(--white);
    border-radius: 8px;
  }
  .net-weight {
    color: var(--ink);
    font: 700 40px/80px "Libre Baskerville", serif;
    text-align: center;
  }
  .address-line {
    position: absolute;
    left: 0;
    right: 0;
    bottom: 18px;
    text-align: center;
    color: var(--white);
    font: 500 13px/1 "Archivo", sans-serif;
    letter-spacing: 0.3px;
  }
</style>
</head>
<body>
  <section class="label">
    <svg class="label-art" viewBox="0 0 1100 520" xmlns="http://www.w3.org/2000/svg">
      <defs>
        <linearGradient id="swirl-tone" x1="0" y1="0" x2="1" y2="1">
          <stop offset="0" stop-color="#a9c8ef"/>
          <stop offset="0.45" stop-color="#3f78d0"/>
          <stop offset="1" stop-color="#1f4fae"/>
        </linearGradient>
        <linearGradient id="crystal-tone" x1="0" y1="0" x2="0" y2="1">
          <stop offset="0" stop-color="#3f78d0"/>
          <stop offset="1" stop-color="#1f4fae"/>
        </linearGradient>
      </defs>
      <rect class="water-backdrop" x="0" y="0" width="1100" height="520" fill="url(#swirl-tone)" role="img" aria-label="Flowing blue water background"/>
      <path class="crystal-field" d="M0 370 C 260 330, 520 320, 760 335 C 900 344, 1010 355, 1100 350 L 1100 520 L 0 520 Z" fill="url(#crystal-tone)" role="img" aria-label="Scattered white salt crystals"/>
    </svg>

    <div class="origin-tag">Australian Owned and Manufactured</div>
    <div class="brand-name">Tarkozel</div>
    <div class="product-name">dishwasher salt</div>
    <div class="weight-panel"><div class="net-weight">2kg</div></div>
    <div class="address-line">17 Maddock St, Kelbury Heights, Queensland, Australia / www.tarkozel.com.au</div>
  </section>
</body>
</html>
```